Design business card for new business which advocates for elders in nursing homes or personal care h

New business for rights of the elderly residents who reside in personal care homes and or nursing homes. I am looking for a business card with logo of keystone for Pennsylvania and something in side the keystone that represents healthcare, advocates, something on that line; monitor care received and needs of resident. Chart audits, State Regulation compliance

Target Market(s)

Seniors no longer safe to live at home by themselves along with their kids

Industry/Entity Type

Business

Contact Information for Business Card

Keystone symbol to represent Pensylvaoa with some kind of symbol inside to represent advocate, seniors, or healthcare symbol

Font styles to use
Serif

Colors
33a6d7
85cae6
abd037

Requirements
Must have
• Brightwell Elder Allies is our business name; our tag line is Path to Better Living
Nice to have
• Nice logo

```html
<!DOCTYPE html>
<html lang="en">
<head>
<meta charset="utf-8">
<title>Brightwell Elder Allies – Business Card</title>
<link rel="stylesheet" href="https://fonts.googleapis.com/css2?family=Alegreya:ital,wght@0,500;1,400&family=Righteous&display=swap">
<style>
  :root {
    --page: #ffffff;
    --card-light: #e3ecec;
    --card-mid: #cfdedf;
    --card-edge: #a9c2c5;
    --teal: #2fc3d3;
    --teal-icon: #7ff0ea;
    --ink: #5d686c;
    --dot: #111111;
    --shadow: rgba(0, 0, 0, 0.55);
  }
  * { margin: 0; padding: 0; box-sizing: border-box; }
  html, body {
    width: 1200px; height: 702px; overflow: hidden;
    background: var(--page);
  }
  .canvas { position: relative; width: 1200px; height: 702px; }
  .card {
    position: absolute; left: 59px; top: 56px; width: 1084px; height: 572px;
    background: radial-gradient(ellipse 70% 85% at 40% 55%, var(--card-light) 0%, var(--card-mid) 55%, var(--card-edge) 100%);
    overflow: hidden;
  }
  .card-title {
    position: absolute; left: 0; right: 0; top: 56px;
    text-align: center;
    font-family: "Righteous", sans-serif;
    font-size: 68px; letter-spacing: 2px; line-height: 1;
    text-transform: uppercase; font-weight: 400;
    color: var(--teal);
  }
  .title-shadow {
    position: absolute; left: 90px; top: 126px; width: 820px; height: 16px;
    background: radial-gradient(ellipse 50% 50% at 50% 50%, var(--shadow), transparent 70%);
  }
  .brand-mark {
    position: absolute; left: 60px; top: 180px; width: 374px; height: 340px;
    display: flex; flex-direction: column; align-items: center; justify-content: center;
  }
  .brand-square { width: 96px; height: 96px; background: var(--teal); margin-bottom: 22px; }
  .brand-name {
    font-family: "Alegreya", serif; font-weight: 500;
    font-size: 52px; line-height: 1.05; text-align: center;
    color: var(--teal);
  }
  .brand-tagline {
    margin-top: 16px;
    font-family: "Alegreya", serif; font-style: italic; font-weight: 400;
    font-size: 28px; line-height: 1; text-align: center;
    color: var(--ink);
  }
  .brand-shadow {
    position: absolute; left: 110px; top: 528px; width: 280px; height: 18px;
    background: radial-gradient(ellipse 50% 50% at 50% 50%, var(--shadow), transparent 70%);
  }
  .divider { position: absolute; left: 454px; top: 184px; }
  .contact-icon { position: absolute; }
  .contact-line {
    position: absolute; left: 599px;
    font-family: "Alegreya", serif; font-style: italic; font-weight: 400;
    font-size: 38px; line-height: 1; color: var(--ink);
    font-variant-numeric: lining-nums;
    white-space: nowrap;
  }
</style>
</head>
<body>
<div class="canvas">
  <div class="card">
    <h1 class="card-title">Brightwell Elder Allies</h1>
    <div class="title-shadow"></div>

    <div class="brand-mark">
      <div class="brand-square"></div>
      <div class="brand-name">Brightwell<br>Elder Allies</div>
      <div class="brand-tagline">Path to Better Living</div>
    </div>
    <div class="brand-shadow"></div>

    <svg class="divider" width="8" height="335" viewBox="0 0 8 335">
      <line x1="4" y1="3" x2="4" y2="332" stroke="var(--dot)" stroke-width="4.5" stroke-linecap="round" stroke-dasharray="0 20.5"/>
    </svg>

    <svg class="contact-icon" style="left:503px;top:165px" width="44" height="74" viewBox="0 0 42 74" aria-hidden="true">
      <path d="M21 0C9 0 0 9 0 21c0 16 21 53 21 53s21-37 21-53C42 9 33 0 21 0z" fill="var(--teal-icon)"/>
      <circle cx="21" cy="20" r="8" fill="var(--card-mid)"/>
    </svg>
    <div class="contact-line" style="top:180px">Address Line1</div>
    <div class="contact-line" style="top:233px">Address Line2</div>

    <svg class="contact-icon" style="left:503px;top:300px" width="58" height="50" viewBox="0 0 50 50" preserveAspectRatio="none" aria-hidden="true">
      <path d="M2 14c0-8 46-8 46 0v6h-11v-5H13v5H2z" fill="var(--teal-icon)"/>
      <path d="M10 22h30l8 26H2z" fill="var(--teal-icon)"/>
      <g fill="var(--card-mid)">
        <circle cx="19" cy="30" r="2.2"/><circle cx="25" cy="30" r="2.2"/><circle cx="31" cy="30" r="2.2"/>
        <circle cx="19" cy="36" r="2.2"/><circle cx="25" cy="36" r="2.2"/><circle cx="31" cy="36" r="2.2"/>
        <circle cx="19" cy="42" r="2.2"/><circle cx="25" cy="42" r="2.2"/><circle cx="31" cy="42" r="2.2"/>
      </g>
    </svg>
    <div class="contact-line" style="top:323px">0000-000-000</div>

    <svg class="contact-icon" style="left:511px;top:380px" width="42" height="67" viewBox="0 0 40 68" preserveAspectRatio="none" aria-hidden="true">
      <rect x="0" y="0" width="40" height="68" rx="6" fill="var(--teal-icon)"/>
      <rect x="5" y="9" width="30" height="44" fill="var(--card-mid)"/>
      <circle cx="20" cy="60" r="3.5" fill="var(--card-mid)"/>
    </svg>
    <div class="contact-line" style="top:401px">0000-000-000</div>

    <svg class="contact-icon" style="left:500px;top:479px" width="66" height="48" viewBox="0 0 64 48" preserveAspectRatio="none" aria-hidden="true">
      <rect x="0" y="0" width="64" height="48" fill="var(--teal-icon)"/>
      <path d="M2 2l30 26L62 2M2 46l22-22M62 46L40 24" fill="none" stroke="var(--card-mid)" stroke-width="3"/>
    </svg>
    <div class="contact-line" style="top:484px">brightwellea@email.com</div>
  </div>
</div>
</body>
</html>
```